Family Conference for a Church needs a creative & colorful flyer

We need a flyer that depicts the following information to be uploaded to our church website and church facebook in order to draw maximum attention. The image should be jpg format so that it can be easily uploaded.
Information to be added in the flyer: Please be creative !!!
1. The Second Annual
2. VARESH ANTO ( this is our brand name of the conference so please be creative in exhibiting this out )
3. Parish Family Conference
4. Growing together in Christ
5. One Church One Family One Vision
6. Presiding Spiritual Father : His Grace Dr. Theodoric Bel Ushan
7. Join us for WORSHIP, RETREAT MESSAGE, INTERACTIVE SESSIONS, WORKSHOPS
8. Save the date : Saturday November 2, 2013
9. CONTACT: Rev. Fr. K.R. Tomlan HLTRC 2857 Penderwick Lane, Aldenmoor QR 19387
I have uploaded a flyer called ONE for your guide only. Use that as your reference, for example ONE is VARESH ANTO for our flyer. I want my flyer to be better than that.
Second upload is a picture which I would like to be added to the flyer as a watermark effect but at the same time visible like a black & white picture or what ever is the best that you feel.
The flyer should be printable and be easily uploaded to facebook. ( jpg image )
Church people of all ages
Church

```html
<!DOCTYPE html>
<html lang="en">
<head>
<meta charset="utf-8">
<title>Varesh Anto Parish Family Conference</title>
<link href="https://fonts.googleapis.com/css2?family=Marcellus&family=Aldrich&family=Exo+2:wght@300;400;600&display=swap" rel="stylesheet">
<style>
  :root {
    --crimson: #cc0a2f;
    --brown: #6b3d12;
    --gold: #f2c230;
    --white: #ffffff;
    --page: #ffffff;
    --edge: #d8d8d8;
  }
  * { margin: 0; padding: 0; box-sizing: border-box; }
  html, body {
    width: 1200px; height: 1000px; overflow: hidden;
    background: var(--page);
  }
  .flyer {
    position: absolute; left: 278px; top: 40px;
    width: 644px; height: 910px;
    background: var(--white);
    border: 1px solid var(--edge);
    overflow: hidden;
    font-family: "Aldrich", "Exo 2", sans-serif;
  }
  .band { position: absolute; left: 0; width: 100%; background: var(--crimson); }
  .band--top { top: 0; height: 371px; }
  .band--bottom { top: 778px; height: 132px; }
  .dove {
    position: absolute; left: 395px; top: 125px; width: 230px; height: 330px;
    border-radius: 50% 50% 45% 55% / 40% 40% 60% 60%;
    background: linear-gradient(180deg, rgba(255,255,255,0.85) 0%, rgba(255,255,255,0.7) 70%, rgba(204,10,47,0.3) 100%);
  }
  .abs { position: absolute; white-space: nowrap; }
  .kicker { left: 40px; top: 36px; font-family: "Exo 2", sans-serif; font-weight: 300; font-size: 17px; color: var(--white); }
  .brand { left: 36px; font-family: "Marcellus", serif; font-size: 108px; line-height: 1; color: var(--white); letter-spacing: 1px; }
  .brand--one { top: 54px; }
  .brand--two { top: 152px; }
  .subtitle { left: 40px; top: 272px; font-family: "Exo 2", sans-serif; font-weight: 300; font-size: 30px; color: var(--gold); }
  .event { left: 38px; top: 303px; font-family: "Exo 2", sans-serif; font-weight: 300; font-size: 47px; color: var(--white); }
  .theme { left: 34px; top: 418px; font-family: "Exo 2", sans-serif; font-weight: 600; font-size: 27px; color: var(--crimson); }
  .pillars {
    position: absolute; left: 33px; top: 456px; width: 576px;
    display: flex; justify-content: space-between;
    font-size: 27px; line-height: 34px; color: var(--brown); white-space: nowrap;
  }
  .label { font-size: 16px; color: var(--brown); line-height: 22px; letter-spacing: 0.5px; }
  .value { font-size: 21px; color: var(--crimson); line-height: 31px; }
  .label--father { left: 34px; top: 546px; }
  .value--father { left: 250px; top: 540px; line-height: 29px; }
  .label--join { left: 34px; top: 638px; }
  .value--join { left: 251px; top: 635px; }
  .label--date { left: 24px; top: 761px; color: var(--crimson); }
  .label--contact { left: 250px; top: 761px; color: var(--crimson); }
  .footer-text { top: 794px; font-size: 20px; line-height: 26px; color: var(--white); }
  .footer-text--date { left: 24px; }
  .footer-text--contact { left: 252px; }
</style>
</head>
<body>
  <main class="flyer">
    <div class="band band--top"></div>
    <div class="band band--bottom"></div>

    <p class="abs kicker">The Second Annual</p>
    <h1>
      <span class="abs brand brand--one">VARESH</span>
      <span class="abs brand brand--two">ANTO</span>
    </h1>
    <div class="dove" role="img" aria-label="Illustration of a white dove in flight"></div>
    <p class="abs subtitle">PARISH FAMILY</p>
    <p class="abs event">Conference</p>

    <p class="abs theme">Growing together in Christ</p>
    <div class="pillars"><span>ONE CHURCH</span><span>ONE FAMILY</span><span>ONE VISION</span></div>

    <p class="abs label label--father">PRESIDING<br>SPIRITUAL FATHER :</p>
    <p class="abs value value--father">His Grace Dr. Theodoric<br>Bel Ushan</p>

    <p class="abs label label--join">JOIN US FOR:</p>
    <p class="abs value value--join">Worship, Retreat Message,<br>Interactive Sessions, Workshops</p>

    <p class="abs label label--date">SAVE THE DATE</p>
    <p class="abs label label--contact">CONTACT</p>
    <p class="abs footer-text footer-text--date">Saturday<br>November 2,<br>2013</p>
    <p class="abs footer-text footer-text--contact">Rev. Fr. K.R. Tomlan HLTRC<br>2857 Penderwick Lane,<br>Aldenmoor QR 19387</p>
  </main>
</body>
</html>
```